PowerPoint template for Credit Card Processor

We need a powerpoint template for our new credit card processing company. Our goal is to sign up merchants to accept credit cards. We will be making presentations to merchants to get them to sign up for our services.

We already have a logo designed. We'd like to incorporate that logo and color scheme in the powerpoint template. The logo file is an illustrator file.

I generally like light colored backgrounds. Nothing too dark.

Industry/Entity Type

Credit Card

Requirements
Must have
• our logo

```html
<!DOCTYPE html>
<html lang="en">
<head>
<meta charset="utf-8">
<title>Merchant Presentation Slide</title>
<link rel="stylesheet" href="https://fonts.googleapis.com/css2?family=Arimo:wght@400;700&family=Open+Sans:wght@700&display=swap">
<style>
  :root {
    --accent-blue: #4f81bd;
    --button-blue: #558ed5;
    --next-blue: #1fb0e6;
    --band-gray: #d9d9d9;
    --panel-blue: #b9cde5;
    --ink: #000000;
    --body-gray: #595959;
    --rule-gray: #8c8c8c;
    --card-dark: #0d3f8f;
    --card-light: #2a63b8;
    --white: #ffffff;
  }
  * { margin: 0; padding: 0; box-sizing: border-box; }
  html, body { width: 1200px; height: 900px; overflow: hidden; background: var(--white); }
  .slide {
    position: relative;
    width: 1200px;
    height: 900px;
    background: var(--white);
    font-family: "Arimo", Arial, sans-serif;
    overflow: hidden;
  }
  .next-link {
    position: absolute;
    top: 6px;
    right: 14px;
    display: flex;
    align-items: center;
    gap: 8px;
    font-size: 26px;
    letter-spacing: 1px;
    color: var(--next-blue);
  }
  .header-band {
    position: absolute;
    top: 48px;
    left: 0;
    width: 1200px;
    height: 198px;
    background: var(--band-gray);
  }
  .main-header {
    position: absolute;
    left: 13px;
    top: 10px;
    font-size: 55px;
    font-weight: 700;
    color: var(--accent-blue);
    line-height: 1;
  }
  .sub-header-1 {
    position: absolute;
    left: 13px;
    top: 76px;
    font-size: 42px;
    font-weight: 700;
    color: var(--ink);
    line-height: 1;
  }
  .sub-header-2 {
    position: absolute;
    left: 13px;
    top: 130px;
    font-size: 29px;
    color: var(--ink);
    line-height: 1;
  }
  .learn-more {
    position: absolute;
    left: 951px;
    top: 130px;
    width: 201px;
    height: 48px;
    border-radius: 6px;
    background: var(--button-blue);
    color: var(--white);
    font-family: "Open Sans", Arial, sans-serif;
    font-weight: 700;
    font-size: 24px;
    display: flex;
    align-items: center;
    justify-content: center;
  }
  .text-block { position: absolute; }
  .text-block h2 {
    font-size: 30px;
    font-weight: 700;
    color: var(--accent-blue);
    line-height: 36px;
  }
  .text-block ul { list-style: none; }
  .text-block li {
    position: relative;
    font-size: 28px;
    line-height: 35.5px;
    color: var(--body-gray);
    padding-left: 38px;
  }
  .text-block li::before {
    content: "•";
    position: absolute;
    left: 4px;
    font-size: 22px;
  }
  .block-one { left: 36px; top: 268px; }
  .block-one li { padding-left: 38px; }
  .block-two {
    left: 20px;
    top: 452px;
    width: 561px;
    height: 160px;
    background: var(--panel-blue);
    padding: 8px 0 0 12px;
  }
  .block-three { left: 32px; top: 666px; }
  .card-visual {
    position: absolute;
    left: 812px;
    top: 616px;
    width: 335px;
    height: 211px;
    border-radius: 11px;
    background: linear-gradient(150deg, var(--card-light), var(--card-dark));
  }
  .footer-rule {
    position: absolute;
    left: 0;
    top: 857px;
    width: 1200px;
    height: 24px;
  }
  .brand {
    position: absolute;
    left: 466px;
    top: 849px;
    height: 40px;
    padding: 0 8px;
    background: var(--white);
    display: flex;
    align-items: center;
    gap: 8px;
    font-size: 30px;
    color: #4d4d4d;
  }
  .brand-mark {
    width: 26px;
    height: 26px;
    border-radius: 50%;
    background: var(--next-blue);
  }
</style>
</head>
<body>
<main class="slide">
  <div class="next-link">
    <span>next</span>
    <svg width="14" height="18" viewBox="0 0 14 18" aria-hidden="true"><path d="M0 0 L14 9 L0 18 Z" fill="var(--next-blue)"/></svg>
  </div>

  <header class="header-band">
    <h1 class="main-header">MAIN HEADER</h1>
    <p class="sub-header-1">Sub header 1</p>
    <p class="sub-header-2">Sub header 2</p>
    <div class="learn-more">Learn More</div>
  </header>

  <section class="text-block block-one">
    <h2>Plain Text</h2>
    <ul><li>Line 1</li><li>Line 2</li><li>Line 3</li></ul>
  </section>

  <section class="text-block block-two">
    <h2>Plain Text</h2>
    <ul><li>Line 1</li><li>Line 2</li><li>Line 3</li></ul>
  </section>

  <section class="text-block block-three">
    <h2>Plain Text</h2>
    <ul><li>Line 1</li><li>Line 2</li><li>Line 3</li></ul>
  </section>

  <div class="card-visual" role="img" aria-label="Illustration of a blue payment card with chip and world map"></div>

  <svg class="footer-rule" viewBox="0 0 1200 24" aria-hidden="true">
    <line x1="32" y1="12" x2="1182" y2="12" stroke="var(--rule-gray)" stroke-width="1" stroke-dasharray="2 2"/>
    <path d="M31 7 L36 12 L31 17 L26 12 Z" fill="var(--rule-gray)"/>
    <path d="M1182 7 L1187 12 L1182 17 L1177 12 Z" fill="var(--rule-gray)"/>
  </svg>

  <div class="brand">
    <span class="brand-mark"></span>
    <span class="brand-name">SwipeLane.net</span>
  </div>
</main>
</body>
</html>
```